Commercial janitorial cleaning

Janitorial cleaning particularly for commercial buildings. Website needs to specify free estimates. Location of service is Hudson, Valatie, East Greenbush, Troy, Albany ny area. Services page with Janitorial services- General Office Cleaning, Construction Cleaning, Carpet Extraction, Consultation/Business, Lighting Maintenance, Seasonal Deep Cleaning, Window cleaning, Event Cleaning, Floor and Carpet Cleaning, Floor Striping and Waxing. Contact us page with email phone number on page and a request page that emails me if they have any questions. About us page-the picture of my family on it with a section I can type a story myself.

Target Market(s)

Commercial businesses

Industry/Entity Type

Janitorial Service

Number of Pages Required

4 page

Font styles to use
Serif
Sans Serif
Script

Colors
ec1f27
1b1b1b
ffffff
9d9d9d

Requirements
Must have
• Phone number 555-314-2760. Must have free estimates on home page. Going for industrial / modern look to website
Nice to have
• Logo is a red and black building so if those colors could be coordinated to website that would be awesome.

```html
<!DOCTYPE html>
<html lang="en">
<head>
<meta charset="utf-8">
<title>Brightline Cleaning Services</title>
<link rel="stylesheet" href="https://fonts.googleapis.com/css2?family=Michroma&family=Open+Sans:ital,wght@0,400;0,600;0,700;0,800;1,600&display=swap">
<style>
:root{
  --red:#ec1f27;
  --red-dark:#c4161d;
  --ink:#1b1b1b;
  --white:#ffffff;
  --grey:#9d9d9d;
  --grey-pale:#f3f3f3;
  --text:#3a3a3a;
}
*{box-sizing:border-box;margin:0;padding:0}
html,body{width:1200px;height:3025px;overflow:hidden}
body{position:relative;background:var(--white);font-family:"Open Sans",Arial,sans-serif;color:var(--text)}
.abs{position:absolute}
.btn{position:absolute;background:linear-gradient(var(--red),var(--red-dark));color:var(--white);font-weight:700;font-size:17px;display:flex;align-items:center;justify-content:center;border-radius:6px;box-shadow:0 8px 10px -6px rgba(0,0,0,.45)}

/* header */
.topbar{left:646px;top:16px;width:514px;height:40px;background:var(--red);border-radius:0 0 0 14px;display:flex;align-items:center;gap:18px;padding-left:28px;color:var(--white);font-size:14px;font-weight:600;white-space:nowrap}
.topbar .item{display:flex;align-items:center;gap:8px}
.social{display:flex;gap:6px;margin-left:4px}
.social span{width:22px;height:22px;border:2px solid var(--white);border-radius:50%}
.brand{left:50px;top:50px;display:flex;align-items:center;gap:14px}
.brand .mark{width:52px;height:70px;background:var(--red)}
.brand .name{font-weight:800;font-size:24px;line-height:1.1;color:var(--red);letter-spacing:.5px}
.nav{left:662px;top:82px;display:flex;gap:22px;font-size:14px;font-weight:700;color:var(--ink);white-space:nowrap}
.nav a{color:inherit;text-decoration:none;padding-bottom:6px}
.nav a.active{border-bottom:3px solid var(--red)}

/* hero */
.hero{left:16px;top:135px;width:1170px;height:551px;background:linear-gradient(160deg,#6b0f1a 0%,#b24a5c 35%,#e9b9c1 55%,#b24a5c 78%,#5e0c16 100%);box-shadow:0 14px 14px -8px rgba(0,0,0,.35)}
.hero h1{position:absolute;left:0;right:0;top:180px;text-align:center;font-family:"Michroma",Arial,sans-serif;font-weight:400;font-size:32px;line-height:40px;color:var(--white);text-shadow:0 2px 3px rgba(0,0,0,.7);letter-spacing:1px}
.hero .btn{left:456px;top:316px;width:258px;height:42px;font-size:21px;border-radius:2px}

/* section titles */
.title{position:absolute;left:0;width:1200px;display:flex;justify-content:center;align-items:center;gap:12px;font-weight:700;font-size:25px;color:var(--ink)}
.title::before,.title::after{content:"";width:70px;height:1px;background:var(--grey)}
.title .sq{width:26px;height:34px;background:var(--red)}
.title em{font-style:normal;color:var(--red)}

/* about */
.about-photo{left:30px;top:762px;width:222px;height:307px;background:linear-gradient(#f2f2f2,#d8dde6);border-radius:4px}
.about-text{left:282px;top:816px;width:466px;font-size:13px;line-height:20.5px;color:#333}
.estimate{left:817px;top:762px;width:337px;height:358px;background:var(--grey-pale);box-shadow:0 12px 12px -6px rgba(0,0,0,.3)}
.estimate .head{height:48px;background:var(--red);color:var(--white);font-weight:700;font-size:17px;display:flex;align-items:center;justify-content:center}
.field{position:absolute;left:30px;display:flex;gap:6px}
.field .ico{width:28px;height:32px;background:#ddd;border:1px solid #ccc;display:flex;align-items:center;justify-content:center}
.field .box{width:242px;height:32px;background:var(--white);border:1px solid #ccc;font-size:11px;padding:8px 12px;color:#333}
.estimate .send{position:absolute;left:66px;top:314px;width:186px;height:28px;background:var(--ink);color:var(--white);font-size:12px;font-weight:700;display:flex;align-items:center;justify-content:center}

/* how it works */
.how{left:16px;top:1206px;width:1170px;height:353px;background:linear-gradient(90deg,#d9dadc,#eeeff0 40%,#e6e7e9 70%,#d3d6da)}
.step{position:absolute;width:270px;text-align:center;font-size:14px;line-height:21px;color:#2a2a2a}
.step svg{display:block;margin:0 auto 22px}

/* services */
.svc{position:absolute;width:130px;text-align:center;font-size:13px;font-weight:700;line-height:17px;color:var(--ink)}
.svc .ring{width:82px;height:82px;border-radius:50%;margin:0 auto 8px;border:3px solid var(--white);box-shadow:0 0 0 2px #444;display:flex;align-items:center;justify-content:center}
.svc .ring.r{background:var(--red)}
.svc .ring.k{background:var(--ink)}

/* testimonials */
.testi{left:16px;top:2037px;width:1170px;height:403px;background:linear-gradient(#f4f4f4,#dfe2e6 60%,#cfd3d8)}
.quote{left:258px;top:2168px;width:686px;height:142px;background:rgba(255,255,255,.92);border-radius:8px;box-shadow:0 4px 10px rgba(0,0,0,.2);padding:22px 40px 0 56px;font-size:13px;line-height:20px;color:#333}
.quote .open{position:absolute;left:18px;top:14px;font-family:Georgia,serif;font-weight:700;font-size:50px;color:var(--ink);line-height:1}
.quote .close{font-family:Georgia,serif;font-weight:700;font-size:40px;color:var(--ink);line-height:0;vertical-align:-14px;margin-left:8px}
.author{left:256px;top:2326px;font-size:13px;font-weight:600;font-style:italic;color:var(--ink)}
.dots{left:570px;top:2372px;display:flex;gap:5px}
.dots span{width:12px;height:12px;border-radius:50%;border:1px solid var(--grey);background:var(--white)}
.dots span.on{background:var(--red);border-color:var(--red)}

/* newsletter */
.news{left:16px;top:2440px;width:1170px;height:202px;background:linear-gradient(90deg,#1b1b1b,#2a2e30 60%,#3b4446)}
.news h2{position:absolute;left:186px;top:70px;font-size:26px;font-weight:700;color:var(--white)}
.news .input{position:absolute;left:597px;top:65px;width:355px;height:40px;background:var(--white);font-size:14px;padding:11px 16px;color:#222}
.news .go{position:absolute;left:960px;top:65px;width:133px;height:40px;background:var(--red);color:var(--white);font-weight:700;font-size:18px;display:flex;align-items:center;justify-content:center}

/* footer */
.foot-tab{left:383px;top:2606px;width:434px;height:80px;background:var(--white);border-radius:60px 60px 0 0}
.foot-brand{left:435px;top:2624px;display:flex;align-items:center;gap:12px}
.foot-brand .mark{width:46px;height:64px;background:var(--red)}
.foot-brand .name{font-weight:800;font-size:22px;line-height:1.15;color:var(--red)}
.foot-person{left:20px;top:2551px;width:212px;height:454px;background:linear-gradient(#c9b9a0,#e4ddd2 40%,#f0e19a 80%,#9fd0e8)}
.col h4{font-size:15px;font-weight:700;color:var(--red);padding-bottom:14px;border-bottom:1px solid #ccc;margin-bottom:16px;letter-spacing:.5px}
.col li{list-style:none;font-size:12.5px;line-height:20px;color:var(--ink);text-transform:uppercase;white-space:nowrap}
.contact-box{left:881px;top:2743px;width:275px;height:202px;border:3px solid var(--red);border-radius:8px;text-align:center}
.contact-box h4{margin-top:18px;font-size:16px;font-weight:800;color:var(--ink)}
.contact-box .phone{display:flex;justify-content:center;align-items:center;gap:8px;margin-top:4px;font-size:28px;font-weight:600;color:var(--red)}
.contact-box .mail{display:flex;justify-content:center;align-items:center;gap:6px;margin-top:22px;font-size:12px;color:var(--ink)}
.contact-box .cta{position:absolute;left:48px;top:156px;width:178px;height:26px;background:var(--red);color:var(--white);font-size:12px;font-weight:700;display:flex;align-items:center;justify-content:center}
.copyright{left:0;top:2985px;width:1200px;height:30px;background:#d7d7d7;font-size:11px;font-weight:600;color:#555;display:flex;align-items:center;justify-content:center;letter-spacing:.5px}
</style>
</head>
<body>

<!-- header -->
<div class="abs topbar">
  <span class="item">
    <svg width="20" height="20" viewBox="0 0 20 20"><circle cx="10" cy="10" r="9" fill="none" stroke="#fff" stroke-width="1.6"/><path d="M7 5.5l2 2-1 1.3a6 6 0 0 0 2.6 2.6l1.3-1 2 2-1.3 1.4C9.9 13.6 6.4 10 6 7.1z" fill="#fff"/></svg>
    555.314.2760
  </span>
  <span class="item">
    <svg width="20" height="20" viewBox="0 0 20 20"><circle cx="10" cy="10" r="9" fill="none" stroke="#fff" stroke-width="1.6"/><rect x="5.5" y="7" width="9" height="6.5" fill="none" stroke="#fff" stroke-width="1.4"/><path d="M5.5 7l4.5 3.5L14.5 7" fill="none" stroke="#fff" stroke-width="1.4"/></svg>
    hello@brightlinecleaning.com
  </span>
  <span class="social"><span></span><span></span><span></span></span>
</div>

<div class="abs brand">
  <div class="mark"></div>
  <div class="name">BRIGHTLINE<br>CLEANING SERVICES</div>
</div>

<nav class="abs nav">
  <a class="active">HOME</a><a>ABOUT</a><a>HOW IT WORKS</a><a>SERVICES</a><a>TESTIMONIALS</a><a>CONTACT</a>
</nav>

<!-- hero -->
<section class="abs hero" role="img" aria-label="Red tinted view looking up at office skyscrapers with a faint outline map of the service area">
  <h1>THE LEADER OF COMMERCIAL CLEANING IN<br>ALBANY, HUDSON, TROY, VALATIE AND<br>EAST GREENBUSH AREA.</h1>
  <div class="btn">CONTACT US</div>
</section>

<!-- about -->
<div class="title" style="top:740px"><span class="sq"></span><span>About <em>Us</em></span></div>
<div class="abs about-photo" role="img" aria-label="Janitor in white uniform with a mop and a cleaning cart"></div>
<p class="abs about-text">Lorem ipsum dolor sit amet, consectetuer adipiscing elit, sed diam nonu tincidunt ut laoreet dolore magna aliquam erat volutpat. Ut wisi enim ad nostrud exerci tation ullamcorper suscipit lobortis nisl ut aliquip ex eac. Duis autem vel eum iriure dolor in hendrerit in vulputate velit esse mole illum dolore eu feugiat nulla facilisis at vero eros et accumsan et iusto blandit praesent luptatum zzril delenit augue duis dolore te feugait nulla. Tempor cum soluta nobis eleifend option congue nihil imperdiet doming rat facer possim assum. Typi non habent claritatem insitam; est usus leg eorum claritatem.</p>
<div class="btn" style="left:411px;top:1035px;width:200px;height:40px">Learn More</div>

<aside class="abs estimate">
  <div class="head">GET INSTANT FREE ESTIMATES</div>
  <div class="field" style="top:66px"><span class="ico"><svg width="14" height="16" viewBox="0 0 14 16"><circle cx="7" cy="4.5" r="3.5" fill="#444"/><path d="M0 16c0-5 3-7 7-7s7 2 7 7z" fill="#444"/></svg></span><span class="box">NAME</span></div>
  <div class="field" style="top:108px"><span class="ico"><svg width="16" height="16" viewBox="0 0 16 16"><path d="M3 1l3 3-1.5 2a8 8 0 0 0 5.5 5.5l2-1.5 3 3-2 2C6 15 1 10 1 3z" fill="#444"/></svg></span><span class="box">PHONE NUMBER</span></div>
  <div class="field" style="top:150px"><span class="ico"><svg width="16" height="12" viewBox="0 0 16 12"><rect x="1" y="1" width="14" height="10" fill="none" stroke="#444" stroke-width="1.6"/><path d="M1 1l7 6 7-6" fill="none" stroke="#444" stroke-width="1.6"/></svg></span><span class="box">EMAIL</span></div>
  <div class="field" style="top:192px"><span class="ico"><svg width="16" height="16" viewBox="0 0 16 16"><circle cx="8" cy="8" r="6.5" fill="none" stroke="#444" stroke-width="1.6"/><circle cx="8" cy="8" r="2.5" fill="#444"/></svg></span><span class="box" style="position:relative">SERVICE NEEDED<svg style="position:absolute;right:0;top:0" width="30" height="30" viewBox="0 0 30 30"><line x1="0" y1="0" x2="0" y2="30" stroke="#ccc"/><path d="M10 12h10l-5 6z" fill="#444"/></svg></span></div>
  <div class="field" style="top:234px"><span class="ico"><svg width="8" height="18" viewBox="0 0 8 18"><circle cx="4" cy="3" r="2.2" fill="#444"/><rect x="2" y="7" width="4" height="11" fill="#444"/></svg></span><span class="box" style="height:62px">DETAILS</span></div>
  <div class="send">Get Quote!</div>
</aside>

<!-- how it works -->
<section class="abs how" role="img" aria-label="Faded photo of cleaners mopping stairs and office floors">
  <div class="title" style="left:-16px;top:62px"><span class="sq"></span><span>How It <em>Works</em></span></div>
  <div class="step" style="left:61px;top:140px">
    <svg width="66" height="66" viewBox="0 0 66 66"><path d="M12 16l9 9-4 5a26 26 0 0 0 16 16l5-4 9 9-5 6C25 56 8 40 6 21z" fill="#ec1f27"/><ellipse cx="46" cy="18" rx="16" ry="12" fill="#ec1f27"/><path d="M36 27l-4 7 9-4z" fill="#ec1f27"/><circle cx="40" cy="18" r="2" fill="#fff"/><circle cx="46" cy="18" r="2" fill="#fff"/><circle cx="52" cy="18" r="2" fill="#fff"/></svg>
    Contact us directly by phone at<br>555.314.2760 or fill out the free<br>estimates form online
  </div>
  <div class="step" style="left:448px;top:140px">
    <svg width="66" height="66" viewBox="0 0 66 66"><rect x="13" y="5" width="40" height="56" rx="3" fill="none" stroke="#ec1f27" stroke-width="4"/><rect x="20" y="18" width="20" height="14" fill="none" stroke="#ec1f27" stroke-width="3"/><line x1="20" y1="40" x2="46" y2="40" stroke="#ec1f27" stroke-width="3"/><line x1="20" y1="47" x2="46" y2="47" stroke="#ec1f27" stroke-width="3"/><line x1="20" y1="54" x2="40" y2="54" stroke="#ec1f27" stroke-width="3"/></svg>
    We will send a quote/estimate<br>based on the details on the<br>requested cleaning work
  </div>
  <div class="step" style="left:857px;top:140px">
    <svg width="66" height="66" viewBox="0 0 66 66"><line x1="22" y1="50" x2="40" y2="12" stroke="#ec1f27" stroke-width="5" stroke-linecap="round"/><path d="M8 48h40a8 8 0 0 1 8 8v2H8z" fill="#ec1f27"/><circle cx="50" cy="48" r="7" fill="none" stroke="#ec1f27" stroke-width="4"/></svg>
    Once you agree and confirm, we<br>will start the cleaning. You can just<br>relax and let us do the job
  </div>
</section>

<!-- services -->
<div class="title" style="top:1614px"><span class="sq"></span><span>Our <em>Services</em></span></div>

<div class="svc" style="left:18px;top:1688px"><div class="ring r"><svg width="44" height="44" viewBox="0 0 44 44"><path d="M6 34a12 12 0 0 1 24 0z" fill="#fff"/><path d="M18 22L32 6" stroke="#fff" stroke-width="3" stroke-linecap="round"/><circle cx="12" cy="36" r="3" fill="#fff"/><circle cx="26" cy="36" r="3" fill="#fff"/><rect x="32" y="32" width="8" height="4" fill="#fff"/></svg></div>General Office Cleaning</div>

<div class="svc" style="left:147px;top:1708px"><div class="ring k"><svg width="44" height="44" viewBox="0 0 44 44"><path d="M8 24a14 14 0 0 1 28 0z" fill="#fff"/><rect x="4" y="24" width="36" height="4" fill="#fff"/><rect x="19" y="8" width="6" height="8" fill="#1b1b1b"/><rect x="10" y="32" width="24" height="4" fill="#fff"/></svg></div>Construction Cleaning</div>

<div class="svc" style="left:276px;top:1722px"><div class="ring r"><svg width="44" height="44" viewBox="0 0 44 44"><rect x="8" y="4" width="28" height="36" fill="none" stroke="#fff" stroke-width="3"/><path d="M22 12l8 10-8 10-8-10z" fill="#fff"/></svg></div>Carpet Extraction</div>

<div class="svc" style="left:405px;top:1742px"><div class="ring k"><svg width="44" height="44" viewBox="0 0 44 44"><circle cx="22" cy="17" r="11" fill="none" stroke="#fff" stroke-width="3"/><rect x="17" y="29" width="10" height="4" fill="#fff"/><rect x="18" y="35" width="8" height="3" fill="#fff"/></svg></div>Lighting Maintenance</div>

<div class="svc" style="left:534px;top:1762px"><div class="ring r"><svg width="44" height="44" viewBox="0 0 44 44"><rect x="14" y="16" width="16" height="24" rx="3" fill="#fff"/><rect x="18" y="8" width="8" height="8" fill="#fff"/><path d="M26 8h8v4h-8z" fill="#fff"/><circle cx="38" cy="6" r="1.6" fill="#fff"/><circle cx="38" cy="12" r="1.6" fill="#fff"/></svg></div>Seasonal Deep Cleaning</div>

<div class="svc" style="left:665px;top:1742px"><div class="ring k"><svg width="44" height="44" viewBox="0 0 44 44"><rect x="6" y="6" width="14" height="14" fill="#fff"/><rect x="24" y="6" width="14" height="14" fill="#fff"/><rect x="6" y="24" width="14" height="14" fill="#fff"/><rect x="24" y="24" width="14" height="14" fill="#fff"/></svg></div>Window Cleaning</div>

<div class="svc" style="left:794px;top:1722px"><div class="ring r"><svg width="44" height="44" viewBox="0 0 44 44"><path d="M22 4l5.3 11 12 1.6-8.8 8.3 2.2 12L22 31l-10.7 5.9 2.2-12-8.8-8.3 12-1.6z" fill="#fff"/></svg></div>Event Cleaning</div>

<div class="svc" style="left:923px;top:1702px"><div class="ring k"><svg width="44" height="44" viewBox="0 0 44 44"><line x1="30" y1="4" x2="18" y2="32" stroke="#fff" stroke-width="3" stroke-linecap="round"/><path d="M8 32h20l2 8H6z" fill="#fff"/></svg></div>Floor &amp; Carpet Cleaning</div>

<div class="svc" style="left:1050px;top:1684px"><div class="ring r"><svg width="44" height="44" viewBox="0 0 44 44"><path d="M16 4h12l10 36H6z" fill="#fff"/><rect x="20" y="8" width="4" height="6" fill="#ec1f27"/><rect x="20" y="18" width="4" height="7" fill="#ec1f27"/><rect x="20" y="29" width="4" height="8" fill="#ec1f27"/></svg></div>Floor Striping &amp; Waxing</div>

<div class="btn" style="left:500px;top:1926px;width:202px;height:40px">Learn More</div>

<!-- testimonials -->
<section class="abs testi" role="img" aria-label="Faded group photo of smiling office workers"></section>
<div class="title" style="top:2090px"><span class="sq"></span><span>Customers' <em>Testimonials</em></span></div>
<div class="abs quote">
  <span class="open">&ldquo;</span>
  Lorem ipsum dolor sit amet, consectetuer adipiscing elit, sed diam nonummy nibh euismod tincidunt ut laoreet dolore magna aliquam erat volutpat. Ut wisi enim ad minim veniam, quis nostrud exercitati on ullamcorper suscipit lobortis nisl ut aliquip ex ea commodo consequat. Duis autem vel eum iriure dolor in hendrerit in vulputate velit esse molestie consequat, vel illum dolore eu feugiat nulla facilisis at vero eros et accumsan et iusto odio dignissim qui.<span class="close">&rdquo;</span>
</div>
<div class="abs author">Daniel Marsh</div>
<div class="abs dots"><span class="on"></span><span></span><span></span><span></span></div>

<!-- newsletter -->
<section class="abs news">
  <svg style="position:absolute;left:84px;top:52px" width="78" height="56" viewBox="0 0 78 56"><rect x="3" y="3" width="72" height="50" fill="none" stroke="#fff" stroke-width="4"/><path d="M3 3l36 28L75 3M3 53l26-24M75 53L49 29" fill="none" stroke="#fff" stroke-width="4"/></svg>
  <h2>SUBSCRIBE TO NEWSLETTER</h2>
  <div class="input">Email Address</div>
  <div class="go">SIGN ME UP</div>
</section>

<!-- footer -->
<div class="abs foot-tab"></div>
<div class="abs foot-brand">
  <div class="mark"></div>
  <div class="name">BRIGHTLINE<br>CLEANING SERVICES</div>
</div>
<div class="abs foot-person" role="img" aria-label="Smiling cleaner holding a mop beside a yellow mop bucket"></div>

<div class="abs col" style="left:244px;top:2740px;width:130px">
  <h4>QUICK LINKS</h4>
  <ul><li>Home</li><li>About</li><li>How It Works</li><li>Services</li><li>Testimonials</li><li>Contact</li></ul>
</div>
<div class="abs col" style="left:424px;top:2740px;width:400px">
  <h4>SERVICES</h4>
  <div style="display:flex;gap:20px">
    <ul style="width:200px"><li>General Office Cleaning</li><li>Construction Cleaning</li><li>Carpet Extraction</li><li>Consultation/Business</li><li>Lighting Maintenance</li></ul>
    <ul><li>Seasonal Deep Cleaning</li><li>Window Cleaning</li><li>Event Cleaning</li><li>Floor &amp; Carpet Cleaning</li><li>Floor Stripping &amp; Waxing</li></ul>
  </div>
</div>

<div class="abs contact-box">
  <h4>CONTACT US TODAY</h4>
  <div class="phone">
    <svg width="30" height="30" viewBox="0 0 30 30"><circle cx="15" cy="15" r="13" fill="none" stroke="#ec1f27" stroke-width="2.5"/><path d="M10 8l3 3-1.5 2a9 9 0 0 0 4.5 4.5l2-1.5 3 3-2 2C13 20.5 8.5 16 8 10z" fill="#ec1f27"/></svg>
    555-314-2760
  </div>
  <div class="mail">
    <svg width="16" height="16" viewBox="0 0 16 16"><circle cx="8" cy="8" r="7" fill="none" stroke="#1b1b1b" stroke-width="1.4"/><rect x="4.5" y="5.5" width="7" height="5" fill="none" stroke="#1b1b1b"/><path d="M4.5 5.5L8 8l3.5-2.5" fill="none" stroke="#1b1b1b"/></svg>
    hello@brightlinecleaning.com
  </div>
  <div class="cta">GET FREE ESTIMATES</div>
</div>

<div class="abs copyright">COPYRIGHT © 2017 BRIGHTLINE CLEANING SERVICE. ALL RIGHTS RESERVED.</div>

</body>
</html>
```